New Business Card Design Project

Removed as project is complete.

Target Market(s)

Industry/Entity Type

Business

Requirements
Must have
• Removed as project is complete.
Nice to have
Should not have

```html
<!DOCTYPE html>
<html lang="en">
<head>
<meta charset="utf-8">
<title>Emberline Assurance – Business Card</title>
<link href="https://fonts.googleapis.com/css2?family=Arimo:wght@400;700&display=swap" rel="stylesheet">
<style>
  :root {
    --stage: #1c1c1e;
    --card-black: #0d0b0b;
    --card-white: #f7f7f7;
    --card-white-edge: #e6e6e6;
    --ink: #111111;
    --orange: #e8931e;
    --warm-faint-a: rgba(233, 150, 110, 0.28);
    --warm-faint-b: rgba(240, 210, 120, 0.22);
  }
  * { box-sizing: border-box; margin: 0; padding: 0; }
  html, body {
    width: 1200px;
    height: 984px;
    overflow: hidden;
    background: var(--stage);
    font-family: "Arimo", Arial, sans-serif;
  }
  .sheet {
    position: relative;
    width: 1200px;
    height: 984px;
  }
  .card {
    position: absolute;
    left: 220px;
    width: 760px;
    height: 434px;
    overflow: hidden;
    border-radius: 2px;
  }
  .card--back { top: 40px; background: var(--card-black); }
  .card--front {
    top: 510px;
    background: linear-gradient(135deg, var(--card-white) 0%, var(--card-white) 55%, var(--card-white-edge) 100%);
  }

  .brand {
    position: absolute;
    display: flex;
    align-items: center;
    gap: 14px;
    color: var(--orange);
    font-weight: 400;
    white-space: nowrap;
  }
  .brand__dot {
    border-radius: 50%;
    background: var(--orange);
    flex: none;
  }
  .card--back .brand { left: 90px; top: 150px; font-size: 38px; }
  .card--back .brand__dot { width: 40px; height: 40px; }
  .card--front .brand { left: 52px; top: 44px; font-size: 27px; }
  .card--front .brand__dot { width: 30px; height: 30px; }

  .tagline {
    position: absolute;
    right: 70px;
    top: 250px;
    color: var(--orange);
    font-size: 17px;
    letter-spacing: 4px;
  }

  .contact {
    position: absolute;
    left: 52px;
    top: 140px;
    color: var(--ink);
    font-size: 17px;
    line-height: 1.3;
  }
  .contact__company { font-weight: 700; }
  .contact__lines { margin-top: 20px; }

  .holder {
    position: absolute;
    right: 80px;
    top: 290px;
    text-align: right;
    color: var(--ink);
  }
  .holder__name { font-size: 23px; font-weight: 700; }
  .holder__role { font-size: 17px; margin-top: 4px; }

  .watermark {
    position: absolute;
    right: -60px;
    top: 150px;
    width: 330px;
    height: 330px;
    border-radius: 50%;
    background: linear-gradient(160deg, var(--warm-faint-b), var(--warm-faint-a));
  }
</style>
</head>
<body>
<main class="sheet">
  <section class="card card--back" aria-label="Card back">
    <div class="brand"><span class="brand__dot"></span>Emberline Assurance International</div>
    <p class="tagline">LEADING THE WAY TO COMPLIANCE...</p>
  </section>

  <section class="card card--front" aria-label="Card front">
    <div class="watermark" role="img" aria-label="Faint brand decoration"></div>
    <div class="brand"><span class="brand__dot"></span>Emberline Assurance International</div>
    <div class="contact">
      <p class="contact__company">Emberline Assurance International Pty Ltd</p>
      <p>P.O. Box 2210, Harbour Vale NSW 2051</p>
      <div class="contact__lines">
        <p>+61 (0)100 200 300</p>
        <p>name@emberlineassurance.com</p>
        <p>www.emberlineassurance.com</p>
      </div>
    </div>
    <div class="holder">
      <p class="holder__name">Name Surname</p>
      <p class="holder__role">director CAMS</p>
    </div>
  </section>
</main>
</body>
</html>
```